" Minha empresa presta serviçoes de estética para gordura localizada, celulite, flacidez, rejuvenescimento, botox, preenchimento, redução de Estrias. Será uma marca licenciada para pessoas que queiram meus protocolos de atendimento. "

```html
<!DOCTYPE html>
<html lang="pt-BR">
<head>
<meta charset="utf-8">
<title>Lívia Moraes — Pasta institucional</title>
<link rel="stylesheet" href="https://fonts.googleapis.com/css2?family=Cinzel:wght@400&family=Montserrat:wght@400;500&display=swap">
<style>
  :root {
    --stage: #e8e8e6;
    --paper: #ffffff;
    --ink: #151515;
    --gold: #f2bb12;
    --gold-deep: #c99a0c;
    --text-dark: #2b2b2b;
    --text-muted: #6a6a6a;
    --faint-grey: #ececec;
  }
  * { margin: 0; padding: 0; box-sizing: border-box; }
  html, body { width: 1200px; height: 1200px; overflow: hidden; background: var(--stage); }
  .folder-spread {
    position: absolute; left: 100px; top: 240px;
    width: 1000px; height: 720px;
    display: flex;
    box-shadow: 0 14px 40px rgba(0,0,0,.18);
  }
  .back-cover {
    position: relative; width: 500px; height: 100%;
    background: var(--paper);
  }
  .front-cover {
    position: relative; width: 500px; height: 100%;
    background: var(--ink);
    overflow: hidden;
  }
  .back-cover .decor-area {
    position: absolute; right: 0; top: 60px; width: 300px; height: 440px;
    background: radial-gradient(ellipse at 90% 45%, var(--faint-grey) 0%, rgba(236,236,236,0) 65%);
  }
  .front-cover .decor-area {
    position: absolute; left: 0; top: 40px; width: 360px; height: 480px;
    background: radial-gradient(ellipse at 25% 45%, rgba(120,95,20,.28) 0%, rgba(21,21,21,0) 65%);
  }
  .front-cover .gold-band {
    position: absolute; left: 0; bottom: 0; width: 100%; height: 14px;
    background: var(--gold);
  }
  .brand-lockup {
    position: absolute; left: 0; right: 0; top: 260px;
    text-align: center;
  }
  .brand-mark {
    display: block; margin: 0 auto 14px;
    width: 34px; height: 34px; border-radius: 50%;
    background: var(--gold);
  }
  .brand-name {
    font-family: "Cinzel", serif;
    font-weight: 400; font-size: 34px; letter-spacing: 3px;
    color: #ffffff;
  }
  .brand-tagline {
    margin-top: 6px; padding-left: 120px;
    font-family: "Montserrat", sans-serif;
    font-size: 12px; letter-spacing: 5px; text-transform: uppercase;
    color: var(--gold);
  }
  .back-brand {
    position: absolute; left: 50px; top: 520px; width: 190px;
    text-align: center;
  }
  .back-brand .brand-mark { width: 22px; height: 22px; margin-bottom: 10px; }
  .back-brand .brand-name { font-size: 17px; letter-spacing: 1.5px; color: var(--text-dark); }
  .contact-list {
    position: absolute; left: 262px; top: 508px;
    list-style: none;
    font-family: "Montserrat", sans-serif; font-size: 10px;
    color: var(--text-muted);
  }
  .contact-list li { display: flex; align-items: center; gap: 8px; height: 19px; }
  .contact-icon { width: 10px; height: 10px; flex: none; }
</style>
</head>
<body>
  <main class="folder-spread">
    <section class="back-cover">
      <div class="decor-area" role="img" aria-label="Faint grey curved brand decoration"></div>
      <div class="back-brand">
        <span class="brand-mark"></span>
        <div class="brand-name">LÍVIA MORAES</div>
      </div>
      <ul class="contact-list">
        <li><svg class="contact-icon" viewBox="0 0 10 10"><rect x="0.5" y="2" width="9" height="6.5" fill="none" stroke="var(--gold-deep)"/><path d="M0.5 2 L5 6 L9.5 2" fill="none" stroke="var(--gold-deep)"/></svg>contato@liviamoraes.com.br</li>
        <li><svg class="contact-icon" viewBox="0 0 10 10"><circle cx="5" cy="5" r="4.3" fill="none" stroke="var(--gold-deep)"/><path d="M0.7 5 H9.3 M5 0.7 V9.3" stroke="var(--gold-deep)" stroke-width=".8"/></svg>www.liviamoraes.com.br</li>
        <li><svg class="contact-icon" viewBox="0 0 10 10"><path d="M2 1 L4 1 L4.6 3.2 L3.4 4.2 Q4.5 6 5.8 6.6 L6.8 5.4 L9 6 L9 8 Q9 9 8 9 Q1 8.5 1 2 Q1 1 2 1 Z" fill="var(--gold-deep)"/></svg>00 00000-0000</li>
        <li><svg class="contact-icon" viewBox="0 0 10 10"><path d="M2 1 L4 1 L4.6 3.2 L3.4 4.2 Q4.5 6 5.8 6.6 L6.8 5.4 L9 6 L9 8 Q9 9 8 9 Q1 8.5 1 2 Q1 1 2 1 Z" fill="var(--gold-deep)"/></svg>00 0000-0000</li>
        <li><svg class="contact-icon" viewBox="0 0 10 10"><path d="M5 9.6 Q1.4 5.6 1.4 3.8 A3.6 3.6 0 0 1 8.6 3.8 Q8.6 5.6 5 9.6 Z" fill="var(--gold-deep)"/><circle cx="5" cy="3.8" r="1.3" fill="#fff"/></svg>Rua do Projeto, 999</li>
      </ul>
    </section>
    <section class="front-cover">
      <div class="decor-area" role="img" aria-label="Faint gold curved brand decoration"></div>
      <div class="brand-lockup">
        <span class="brand-mark"></span>
        <div class="brand-name">LÍVIA MORAES</div>
        <div class="brand-tagline">Estética Integral</div>
      </div>
      <div class="gold-band"></div>
    </section>
  </main>
</body>
</html>
```